Mobile Fitness snd Therapy Business Card Design

I need a business card designed for my mobile fitness and therapy business.

Please view the images that I have uploaded. I like the simplicity of the design that I have attached. I adapted it with my information

Target Market(s)

Those seeking personal training, injury rehabilitation or massage therapy.

Industry/Entity Type

Business

Contact Information for Business Card

Dylan Marwick - MSc, CAT(C), RMT, CSCS, Pn2
e-mail: dylan@vantrelo.com
website: www.vantrelo.com
instagram: @dylan_marwick

Font styles to use
Sans Serif

Colors
3176b5
0355a3

Requirements
Must have
• "Contact us to receive a FREE assessment"
• Services offered:
• Personal Training
• Golf Fitness
• Injury Rehab
• Massage Therapy
• Yoga
Nice to have
• Consistent colours with brand
• - Dark Blue: #232837
• - Blue: #5096f0
• Consistent look/feel with the website: www.vantrelo.com

```html
<!DOCTYPE html>
<html lang="en">
<head>
<meta charset="utf-8">
<title>Vantrelo Business Card</title>
<link rel="stylesheet" href="https://fonts.googleapis.com/css2?family=Roboto:wght@400;500;700;900&display=swap">
<style>
  :root{
    --bg:#d9dbe0;
    --navy:#232837;
    --blue:#2f66d8;
    --blue-bright:#5096f0;
    --blue-deep:#0355a3;
    --paper:#f4f4f2;
    --ink:#1d2230;
    --white:#ffffff;
    --muted:#8fb3f0;
  }
  *{box-sizing:border-box;margin:0;padding:0}
  html,body{width:1200px;height:1000px;overflow:hidden}
  body{background:var(--bg);font-family:"Roboto",Arial,sans-serif;position:relative}

  .card{position:absolute;left:215px;width:770px;height:440px;border-radius:26px;overflow:hidden;
        box-shadow:0 10px 30px rgba(20,25,40,.25)}
  .card--back{top:40px;background:var(--navy);color:var(--white)}
  .card--front{top:520px;background:var(--paper);color:var(--ink)}

  .wordmark{position:absolute;font-weight:900;letter-spacing:6px;line-height:1}
  .tagline{position:absolute;font-weight:500;letter-spacing:7px;line-height:1}

  .card--back .wordmark{left:70px;top:50px;font-size:86px;color:var(--white)}
  .card--back .tagline{left:74px;top:148px;font-size:21px;color:var(--white)}

  .services-title{position:absolute;left:330px;top:196px;font-size:14px;color:var(--muted)}
  .service{position:absolute;width:120px;text-align:center}
  .service__icon{display:block;margin:0 auto;width:74px;height:74px;border-radius:50%;
                 background:var(--blue);border:3px solid #4f7fe6}
  .service__label{display:block;margin-top:8px;font-size:13px;font-weight:500;line-height:1.15;text-transform:uppercase}
  .service--training{left:60px;top:280px}
  .service--golf{left:195px;top:245px}
  .service--rehab{left:330px;top:210px;top:222px}
  .service--massage{left:465px;top:178px}
  .service--yoga{left:600px;top:130px}

  .cta{position:absolute;left:330px;top:380px;padding:7px 14px;border:2px solid #cfd3dc;border-radius:6px;
       font-size:19px;font-weight:500;color:var(--white);white-space:nowrap}
  .cta strong{color:var(--blue-bright);font-weight:700}

  .card--front .wordmark{left:250px;top:70px;font-size:80px;color:var(--ink)}
  .card--front .tagline{left:256px;top:162px;font-size:19px;color:var(--ink)}

  .edge-bar{position:absolute;left:0;width:14px;background:var(--blue-bright)}
  .edge-bar--top{top:268px;height:40px}
  .edge-bar--bottom{top:350px;height:70px}

  .person{position:absolute;left:60px;top:255px}
  .person__name{font-size:27px;font-weight:700;color:var(--blue);text-transform:uppercase}
  .person__creds{font-size:15px;font-weight:500;margin-top:4px}

  .contact{position:absolute;left:60px;top:335px;list-style:none}
  .contact li{display:flex;align-items:center;gap:10px;font-size:19px;height:30px}
  .contact svg{width:20px;height:20px;flex:none}
  .contact .accent{color:var(--blue);font-weight:700}
</style>
</head>
<body>

<section class="card card--back" aria-label="Card back">
  <div class="wordmark">VANTRELO</div>
  <div class="tagline">NUTRITION - FITNESS - HEALTH</div>

  <div class="services-title">Services Offered</div>

  <div class="service service--training">
    <span class="service__icon" role="img" aria-label="Dumbbell icon"></span>
    <span class="service__label">Personal<br>Training</span>
  </div>
  <div class="service service--golf">
    <span class="service__icon" role="img" aria-label="Golfer swinging icon"></span>
    <span class="service__label">Golf<br>Fitness</span>
  </div>
  <div class="service service--rehab">
    <span class="service__icon" role="img" aria-label="Injury rehab treatment icon"></span>
    <span class="service__label">Injury<br>Rehab</span>
  </div>
  <div class="service service--massage">
    <span class="service__icon" role="img" aria-label="Massage therapy icon"></span>
    <span class="service__label">Massage<br>Therapy</span>
  </div>
  <div class="service service--yoga">
    <span class="service__icon" role="img" aria-label="Yoga pose icon"></span>
    <span class="service__label">Yoga</span>
  </div>

  <div class="cta">Contact us to receive a <strong>FREE</strong> assessment</div>
</section>

<section class="card card--front" aria-label="Card front">
  <div class="wordmark">VANTRELO</div>
  <div class="tagline">NUTRITION - FITNESS - HEALTH</div>

  <span class="edge-bar edge-bar--top"></span>
  <span class="edge-bar edge-bar--bottom"></span>

  <div class="person">
    <div class="person__name">Dylan Marwick</div>
    <div class="person__creds">MSC, CAT(C), RMT, CSCS, PN2</div>
  </div>

  <ul class="contact">
    <li>
      <svg viewBox="0 0 20 20" aria-hidden="true"><rect x="1" y="4" width="18" height="12" rx="1.5" fill="var(--ink)"/><path d="M1.5 5 10 11 18.5 5" stroke="var(--paper)" stroke-width="1.6" fill="none"/></svg>
      dylan@vantrelo.com
    </li>
    <li>
      <svg viewBox="0 0 20 20" aria-hidden="true"><rect x="2" y="2" width="16" height="16" rx="4" fill="none" stroke="var(--ink)" stroke-width="2"/></svg>
      @dylan_marwick
    </li>
    <li>
      <svg viewBox="0 0 20 20" aria-hidden="true"><circle cx="10" cy="10" r="8" fill="none" stroke="var(--ink)" stroke-width="1.8"/><ellipse cx="10" cy="10" rx="3.5" ry="8" fill="none" stroke="var(--ink)" stroke-width="1.4"/><path d="M2 10h16" stroke="var(--ink)" stroke-width="1.4"/></svg>
      <span>www.<span class="accent">vantrelo</span>.com</span>
    </li>
  </ul>
</section>

</body>
</html>
```